WordPress Website for Pain Relief Clinic

I need a WordPress website designed for my laser pain relief clinic. It needs to be a professional, responsive design with 7 pages: Home, Why Choose Us, Treatable Conditions, Testimonials, FAQ, Franchising, Contact Us. Here is logo: https://files.brivoltcdn.com/media.t-w-e-n.com/sitebuilder/472/CalvexaLogoHighQuality.png

Target Market(s)

people with pain,elderly adults,injuries,soreness

Industry/Entity Type

Clinic

Number of Pages Required

5+ page

Colors
0792cd
85abd2

```html
<!DOCTYPE html>
<html lang="en">
<head>
<meta charset="utf-8">
<title>Calvexa Laser Pain Relief Clinic</title>
<link rel="stylesheet" href="https://fonts.googleapis.com/css2?family=Open+Sans:ital,wght@0,400;0,600;0,700;0,800;1,400&display=swap">
<style>
:root{
  --blue:#0792cd;
  --blue-soft:#85abd2;
  --navy:#17324f;
  --navy-2:#1f4a73;
  --ink:#2e3a46;
  --muted:#7b8794;
  --line:#dfe5eb;
  --paper:#ffffff;
  --tint:#f3f6f9;
  --green:#8cc63f;
  --star:#f5a623;
}
*{box-sizing:border-box;margin:0;padding:0}
html,body{width:1200px;height:2880px;overflow:hidden}
body{font-family:"Open Sans",Arial,sans-serif;color:var(--ink);background:var(--paper);position:relative}
.sec{position:absolute;left:0;width:1200px}
a{color:inherit;text-decoration:none}

/* header */
.site-header{top:0;height:68px;background:var(--paper);border-bottom:1px solid var(--line)}
.brand{position:absolute;left:24px;top:14px;display:flex;align-items:center;gap:10px}
.brand-dot{width:36px;height:36px;border-radius:50%;background:var(--blue)}
.brand-name{font-size:28px;font-weight:700;color:var(--navy);letter-spacing:.5px}
.main-nav{position:absolute;right:24px;top:24px;display:flex;gap:26px;font-size:12px;font-weight:700;color:var(--navy);letter-spacing:.4px}
.main-nav .active{color:var(--blue);border-bottom:2px solid var(--blue);padding-bottom:4px}

/* hero */
.hero{top:68px;height:540px;background:linear-gradient(90deg,#c9d6e0 0%,#e4b9a2 22%,#d08a72 36%,#2d4f72 58%,#17324f 100%)}
.hero-copy{position:absolute;left:820px;top:180px;width:350px;color:#fff}
.hero-kicker{font-size:27px;font-weight:400;letter-spacing:.5px;white-space:nowrap}
.hero-title{font-size:35px;font-weight:800;line-height:1.15;margin-top:2px;white-space:nowrap}
.hero-text{font-size:13px;line-height:1.6;margin-top:14px;color:#dfe8f1}
.btn-outline{display:inline-block;margin-top:22px;border:2px solid #fff;color:#fff;font-size:12px;font-weight:700;padding:10px 18px;letter-spacing:.5px}
.hero-dots{position:absolute;right:28px;bottom:16px;display:flex;gap:8px}
.hero-dots span{width:22px;height:6px;background:rgba(255,255,255,.45)}
.hero-dots span.on{background:#fff}

/* services */
.services{top:608px;height:440px;background:var(--paper)}
.cards{position:absolute;left:72px;top:60px;display:flex;gap:20px}
.card{width:249px}
.card-photo{height:152px}
.card-title{margin-top:14px;font-size:15px;font-weight:800;color:var(--navy);letter-spacing:.3px}
.card-text{margin-top:8px;font-size:12px;line-height:1.55;color:var(--muted)}
.read-more{display:inline-flex;align-items:center;gap:6px;margin-top:10px;font-size:12px;font-weight:600;color:var(--navy)}
.read-more i{width:12px;height:12px;background:var(--blue);display:inline-block}
.pager{position:absolute;left:0;width:1200px;top:380px;display:flex;justify-content:center;align-items:center;gap:14px}
.pager span{width:26px;height:26px;border-radius:50%;border:2px solid var(--line)}
.pager span.on{border-color:var(--blue);background:var(--blue)}

/* welcome */
.welcome{top:1048px;height:468px;background:var(--tint)}
.welcome-box{position:absolute;left:72px;top:40px;width:1056px;height:404px;background:var(--paper)}
.welcome-copy{position:absolute;left:28px;top:28px;width:490px}
.welcome-head{display:flex;align-items:center;gap:12px}
.welcome-dot{width:48px;height:48px;border-radius:50%;background:var(--navy)}
.welcome-sub{font-size:17px;font-weight:600;color:var(--navy)}
.welcome-title{font-size:24px;font-weight:800;color:var(--blue);line-height:1.1}
.welcome-copy p{font-size:12px;line-height:1.65;color:var(--muted);margin-top:14px}
.welcome-photo{position:absolute;right:0;top:0;width:500px;height:404px;background:linear-gradient(135deg,#2b3d55,#c58d6e 45%,#e5b59a 60%,#3c5f86)}

/* events + social */
.news{top:1516px;height:430px;background:var(--paper)}
.col-title{display:flex;align-items:center;gap:10px;font-size:21px;font-weight:800;color:var(--navy)}
.col-title i{width:22px;height:22px;background:var(--blue);display:inline-block}
.col-title i.round{border-radius:50%}
.events{position:absolute;left:72px;top:40px;width:520px}
.event{margin-top:18px}
.event-title{font-size:14px;font-weight:700;color:var(--navy)}
.event-body{display:flex;gap:14px;margin-top:8px}
.event-thumb{width:84px;height:70px;flex:none;background:linear-gradient(135deg,#d7a58a,#7e98b4)}
.event-date{font-size:11px;color:var(--blue);font-weight:600}
.event-text{font-size:11.5px;line-height:1.55;color:var(--muted);margin-top:3px}
.social{position:absolute;left:640px;top:40px;width:488px}
.social-box{margin-top:18px;border:1px solid var(--line);padding:16px;height:300px}
.social-page{display:flex;align-items:center;gap:12px;padding-bottom:12px;border-bottom:1px solid var(--line)}
.social-page-pic{width:48px;height:48px;background:var(--navy)}
.social-page-name{font-size:13px;font-weight:700;color:var(--navy)}
.social-page-meta{font-size:11px;color:var(--muted)}
.social-count{font-size:11px;color:var(--muted);margin:12px 0 8px}
.fans{display:grid;grid-template-columns:repeat(7,56px);gap:8px}
.fan{height:56px;background:linear-gradient(160deg,#c9a28c,#8ea4bb)}
.social-foot{margin-top:12px;font-size:11px;color:var(--muted)}

/* testimonials */
.testimonials{top:1946px;height:420px;background:var(--paper)}
.section-rule{position:absolute;left:0;top:40px;width:1200px;display:flex;justify-content:center;align-items:center;gap:22px;font-size:19px;font-weight:800;color:var(--navy);letter-spacing:.6px}
.section-rule::before,.section-rule::after{content:"";width:100px;height:1px;background:var(--line)}
.quote{position:absolute;left:160px;top:100px;width:880px;text-align:center;font-size:13px;line-height:1.8;color:var(--muted);font-style:italic}
.quote-author{position:absolute;left:0;width:1200px;top:250px;text-align:center;font-size:14px;font-weight:700;color:var(--navy)}
.stars{position:absolute;left:0;width:1200px;top:282px;display:flex;justify-content:center;gap:4px}
.arrow{position:absolute;top:150px;width:30px;height:30px;border-radius:50%;border:1px solid var(--line)}
.arrow.left{left:90px}.arrow.right{right:90px}
.arrow svg{display:block;margin:8px auto}

/* feature strip */
.strip{top:2366px;height:120px;background:var(--navy);display:flex}
.strip-item{flex:1;display:flex;align-items:center;gap:14px;padding:0 26px;border-right:1px solid rgba(255,255,255,.15)}
.strip-item:nth-child(2),.strip-item:nth-child(4){background:var(--navy-2)}
.strip-icon{width:46px;height:46px;border-radius:50%;border:2px solid var(--blue-soft);flex:none}
.strip-title{font-size:15px;font-weight:700;color:#fff}
.strip-text{font-size:11px;color:#b9cbe0;margin-top:3px;line-height:1.4}

/* footer */
.site-footer{top:2486px;height:394px;background:var(--tint)}
.fcol{position:absolute;top:36px}
.fhead{font-size:14px;font-weight:800;color:var(--navy);letter-spacing:.4px;line-height:1.25}
.fhead span{display:block;font-size:21px}
.field{width:210px;height:32px;border:1px solid var(--line);background:#fff;font-size:11px;color:var(--muted);padding:8px 10px;margin-top:10px}
.btn-green{width:210px;height:32px;background:var(--green);color:#fff;font-size:12px;font-weight:700;text-align:center;line-height:32px;margin-top:10px}
.hours dt{font-size:12px;font-weight:700;color:var(--ink);margin-top:14px}
.hours dd{font-size:12px;color:var(--muted)}
.contact-row{display:flex;gap:10px;align-items:flex-start;margin-top:16px;font-size:12px;color:var(--muted);line-height:1.5}
.contact-row svg{flex:none;margin-top:2px}
.foot-brand{display:flex;align-items:center;gap:10px}
.foot-brand .brand-dot{width:40px;height:40px;background:var(--blue-soft)}
.foot-brand .brand-name{font-size:30px;color:var(--muted)}
.legal{font-size:11px;color:var(--muted);line-height:1.6;margin-top:18px}
.footer-base{position:absolute;left:0;bottom:0;width:1200px;height:36px;background:var(--navy)}
</style>
</head>
<body>

<header class="sec site-header">
  <div class="brand"><span class="brand-dot"></span><span class="brand-name">Calvexa</span></div>
  <nav class="main-nav">
    <a class="active">HOME</a><a>WHY CHOOSE US</a><a>TREATABLE CONDITIONS</a><a>TESTIMONIALS</a><a>FAQ</a><a>FRANCHISING</a><a>CONTACT</a>
  </nav>
</header>

<section class="sec hero" role="img" aria-label="Photo of a woman holding her sore shoulder, highlighted in red, on a blue backdrop">
  <div class="hero-copy">
    <div class="hero-kicker">WANT RELIEF FROM</div>
    <div class="hero-title">KNEE-PAIN? TELL US</div>
    <p class="hero-text">In publishing and graphic design, lorem ipsum is a filler text commonly used to demonstrate the graphic elements of a document or visual presentation.</p>
    <a class="btn-outline">BOOK AN APPOINTMENT</a>
  </div>
  <div class="hero-dots"><span class="on"></span><span></span><span></span><span></span></div>
</section>

<section class="sec services">
  <div class="cards">
    <article class="card">
      <div class="card-photo" role="img" aria-label="Photo of a person holding their lower back" style="background:linear-gradient(135deg,#e0b49b,#b96f5b 55%,#8aa3bd)"></div>
      <h3 class="card-title">BACK PAIN</h3>
      <p class="card-text">Nullam ac urna eu felis dapibus condimentum sit amet a augue. Sed non neque elit.</p>
      <a class="read-more"><i></i>Read More</a>
    </article>
    <article class="card">
      <div class="card-photo" role="img" aria-label="Photo of hands holding a painful knee" style="background:linear-gradient(135deg,#d49b83,#c0584a 50%,#e7c8b4)"></div>
      <h3 class="card-title">KNEE PAIN</h3>
      <p class="card-text">Nullam ac urna eu felis dapibus condimentum sit amet a augue. Sed non neque elit.</p>
      <a class="read-more"><i></i>Read More</a>
    </article>
    <article class="card">
      <div class="card-photo" role="img" aria-label="Photo of a sore shoulder highlighted in red" style="background:linear-gradient(135deg,#7d9ab8,#d28670 50%,#b94a3e)"></div>
      <h3 class="card-title">SHOULDER PAIN</h3>
      <p class="card-text">Nullam ac urna eu felis dapibus condimentum sit amet a augue. Sed non neque elit.</p>
      <a class="read-more"><i></i>Read More</a>
    </article>
    <article class="card">
      <div class="card-photo" role="img" aria-label="Photo of a hand holding a sore arm" style="background:linear-gradient(135deg,#efd3c3,#d59a80 55%,#c7d3de)"></div>
      <h3 class="card-title">ARM PAIN</h3>
      <p class="card-text">Nullam ac urna eu felis dapibus condimentum sit amet a augue. Sed non neque elit.</p>
      <a class="read-more"><i></i>Read More</a>
    </article>
  </div>
  <div class="pager"><span></span><span class="on"></span></div>
</section>

<section class="sec welcome">
  <div class="welcome-box">
    <div class="welcome-copy">
      <div class="welcome-head">
        <span class="welcome-dot"></span>
        <div><div class="welcome-sub">Welcome to</div><h2 class="welcome-title">Calvexa Laser Pain Relief</h2></div>
      </div>
      <p>This is a sample of placeholder Lorem Ipsum. Proin gravida nibh vel velit auctor aliquet. Aenean sollicitudin, lorem quis bibendum auctor, nisi elit consequat ipsum, nec sagittis sem nibh id elit. Duis sed odio sit amet nibh vulputate cursus a sit amet mauris. Morbi accumsan ipsum velit. Nam nec tellus a odio tincidunt auctor a ornare odio. Sed non mauris vitae erat consequat auctor eu in elit.</p>
      <p>Nullam ac urna eu felis dapibus condimentum sit amet a augue. Sed non neque elit. Sed ut imperdiet nisi. Proin condimentum fermentum nunc.</p>
      <p>Etiam pharetra, erat sed fermentum feugiat, velit mauris egestas quam, ut aliquam massa nisl quis neque. Suspendisse in orci enim.</p>
      <a class="read-more"><i></i>Read More</a>
    </div>
    <div class="welcome-photo" role="img" aria-label="Photo of a team stacking their hands together"></div>
  </div>
</section>

<section class="sec news">
  <div class="events">
    <h2 class="col-title"><i></i>Upcoming Events</h2>
    <article class="event">
      <h3 class="event-title">Lorem ipsum, giving information on its origins, as well as a random</h3>
      <div class="event-body">
        <div class="event-thumb" role="img" aria-label="Event photo of a patient treatment"></div>
        <div><div class="event-date">28 Nov 2024</div><p class="event-text">This is a sample of placeholder Lorem Ipsum. Proin gravida nibh vel velit auctor aliquet. Aenean sollicitudin, lorem quis bibendum auctor, nisi elit consequat ipsum.</p></div>
      </div>
    </article>
    <article class="event">
      <h3 class="event-title">Lorem ipsum, giving information on its origins, as well as a random</h3>
      <div class="event-body">
        <div class="event-thumb" role="img" aria-label="Event photo of a clinic session"></div>
        <div><div class="event-date">28 Nov 2024</div><p class="event-text">This is a sample of placeholder Lorem Ipsum. Proin gravida nibh vel velit auctor aliquet. Aenean sollicitudin, lorem quis bibendum auctor, nisi elit consequat ipsum.</p></div>
      </div>
    </article>
    <article class="event">
      <h3 class="event-title">Lorem ipsum, giving information on its origins, as well as a random</h3>
      <div class="event-body">
        <div class="event-thumb" role="img" aria-label="Event photo of a therapy demonstration"></div>
        <div><div class="event-date">28 Nov 2024</div><p class="event-text">This is a sample of placeholder Lorem Ipsum. Proin gravida nibh vel velit auctor aliquet. Aenean sollicitudin, lorem quis bibendum auctor, nisi elit consequat ipsum.</p></div>
      </div>
    </article>
  </div>
  <div class="social">
    <h2 class="col-title"><i class="round"></i>Find us on Friendwall</h2>
    <div class="social-box">
      <div class="social-page">
        <div class="social-page-pic"></div>
        <div><div class="social-page-name">Calvexa Laser Pain Relief Clinic</div><div class="social-page-meta">Like Page · 1,204 likes</div></div>
      </div>
      <div class="social-count">326 people like Calvexa Laser Pain Relief Clinic</div>
      <div class="fans" role="img" aria-label="Grid of follower profile pictures">
        <div class="fan"></div><div class="fan"></div><div class="fan"></div><div class="fan"></div><div class="fan"></div><div class="fan"></div><div class="fan"></div>
        <div class="fan"></div><div class="fan"></div><div class="fan"></div><div class="fan"></div><div class="fan"></div><div class="fan"></div><div class="fan"></div>
      </div>
      <div class="social-foot">Social plugin</div>
    </div>
  </div>
</section>

<section class="sec testimonials">
  <h2 class="section-rule">CLIENT TESTIMONIALS</h2>
  <span class="arrow left"><svg width="12" height="12" viewBox="0 0 12 12"><path d="M8 1 3 6l5 5" fill="none" stroke="#7b8794" stroke-width="2"/></svg></span>
  <span class="arrow right"><svg width="12" height="12" viewBox="0 0 12 12"><path d="M4 1l5 5-5 5" fill="none" stroke="#7b8794" stroke-width="2"/></svg></span>
  <p class="quote">Nam nec tellus a odio tincidunt auctor a ornare odio. Sed non mauris vitae erat consequat auctor eu in elit. Class aptent taciti sociosqu ad litora torquent per conubia nostra, per inceptos himenaeos. Mauris in erat justo. Nullam ac urna eu felis dapibus condimentum sit amet a augue. Sed non neque elit. Sed ut imperdiet nisi. Proin condimentum fermentum nunc. Etiam pharetra, erat sed fermentum feugiat, velit mauris egestas quam, ut aliquam massa nisl quis neque. Suspendisse in orci enim.</p>
  <div class="quote-author">- Dana Morrow</div>
  <div class="stars">
    <svg width="90" height="18" viewBox="0 0 90 18">
      <g fill="var(--star)"><path id="st" d="M9 1l2.4 5.2 5.6.6-4.2 3.8 1.2 5.6L9 13.4 4 16.2l1.2-5.6L1 6.8l5.6-.6z"/>
      <use href="#st" x="18"/><use href="#st" x="36"/></g>
      <g fill="#d5dbe1"><use href="#st" x="54"/><use href="#st" x="72"/></g>
    </svg>
  </div>
</section>

<section class="sec strip">
  <div class="strip-item"><span class="strip-icon"></span><div><div class="strip-title">Book An Appointment</div><div class="strip-text">Schedule your laser session online today.</div></div></div>
  <div class="strip-item"><span class="strip-icon"></span><div><div class="strip-title">Our Franchising</div><div class="strip-text">Open a clinic with our proven model.</div></div></div>
  <div class="strip-item"><span class="strip-icon"></span><div><div class="strip-title">What you can Expect?</div><div class="strip-text">See how a first visit works for you.</div></div></div>
  <div class="strip-item"><span class="strip-icon"></span><div><div class="strip-title">Meet The Doctor</div><div class="strip-text">Learn about our caring medical team.</div></div></div>
</section>

<footer class="sec site-footer">
  <div class="fcol" style="left:72px">
    <h3 class="fhead">SUBSCRIBE TO<span>OUR NEWSLETTER</span></h3>
    <div class="field">Enter Name</div>
    <div class="field">Enter Email</div>
    <div class="btn-green">SUBSCRIBE</div>
  </div>
  <div class="fcol" style="left:340px">
    <h3 class="fhead">OFFICE HOURS</h3>
    <dl class="hours">
      <dt>Monday to Friday</dt><dd>9:00am - 6:00pm</dd>
      <dt>Saturday</dt><dd>9:00am - 1:00pm</dd>
      <dt>Sunday</dt><dd>Closed</dd>
    </dl>
  </div>
  <div class="fcol" style="left:560px;width:240px">
    <h3 class="fhead">GET IN TOUCH</h3>
    <div class="contact-row"><svg width="14" height="16" viewBox="0 0 14 16"><path d="M7 15s5-5.2 5-9A5 5 0 0 0 2 6c0 3.8 5 9 5 9z" fill="var(--blue)"/><circle cx="7" cy="6" r="2" fill="#fff"/></svg><span>418 Linden Crest Ave, Suite 12<br>Brookfield, NY 10027</span></div>
    <div class="contact-row"><svg width="14" height="14" viewBox="0 0 14 14"><path d="M3 1h3l1 3-2 1a7 7 0 0 0 4 4l1-2 3 1v3a1 1 0 0 1-1 1A12 12 0 0 1 1 2a1 1 0 0 1 1-1z" fill="var(--blue)"/></svg><span>(555) 014-2290</span></div>
    <div class="contact-row"><svg width="14" height="12" viewBox="0 0 14 12"><rect x="0" y="0" width="14" height="12" rx="1" fill="var(--blue)"/><path d="M1 1l6 5 6-5" fill="none" stroke="#fff" stroke-width="1.4"/></svg><span>hello@calvexaclinic.test</span></div>
  </div>
  <div class="fcol" style="left:860px;width:268px">
    <div class="foot-brand"><span class="brand-dot"></span><span class="brand-name">Calvexa</span></div>
    <p class="legal">© 2024 Calvexa Laser Pain Relief Clinic.<br>All Rights Reserved. Terms &amp; Conditions<br>Privacy Policy | Terms of Use</p>
  </div>
  <div class="footer-base"></div>
</footer>

</body>
</html>
```